Dog grooming business card
This is a business card for m dog grooming business like it say above.
In the priorities box below I will have the text that I want on the card.

Industry/Entity Type

Business

Colors

Designer to choose colors to be used in the design.

Requirements
Must have
• My logo and the insurance stamp must be on the card.

Text it must have :

Professional grooming services
Email: lunabrisk@mailvane.net
Text or call 1 705 318 6642
TKV certified/member
Pet first aid certified
Next appointment ___________________________________
Nice to have
• Greens to match my logo

```html
<!DOCTYPE html>
<html lang="en">
<head>
<meta charset="utf-8">
<title>Luna Brisk – Grooming Business Cards</title>
<link rel="stylesheet" href="https://fonts.googleapis.com/css2?family=Fenix&family=Quicksand:wght@500&family=Open+Sans:wght@700;800&display=swap">
<style>
  :root {
    --green: #8dc03f;
    --green-deep: #5e8f1c;
    --green-text: #86b83a;
    --black: #070707;
    --white: #ffffff;
    --ink: #1a1a1a;
    --page-top: #ffffff;
    --page-bottom: #8cbd3f;
  }
  html, body { margin: 0; padding: 0; overflow: hidden; }
  body {
    width: 927px; height: 1200px; position: relative;
    background:
      repeating-linear-gradient(60deg, transparent 0 180px, rgba(255,255,255,.35) 180px 181px),
      repeating-linear-gradient(-60deg, transparent 0 180px, rgba(255,255,255,.35) 180px 181px),
      linear-gradient(to bottom, var(--page-top) 0%, #dfeccb 35%, var(--page-bottom) 100%);
  }
  .card {
    position: absolute; width: 383px; height: 219px; overflow: hidden;
    background: var(--white); outline: 1px solid #333;
  }
  .card > svg.bg { position: absolute; inset: 0; width: 383px; height: 219px; }
  .brand {
    position: absolute; top: 20px; left: 0; right: 0;
    display: flex; align-items: center; justify-content: center; gap: 6px;
  }
  .brand-dot { width: 34px; height: 34px; border-radius: 50%; background: var(--green); }
  .brand-name { font-family: "Fenix", serif; font-size: 20px; color: var(--green); }
  .line { position: absolute; left: 0; right: 0; text-align: center; white-space: nowrap; }
  .heading { top: 96px; font-family: "Fenix", serif; font-size: 18px; color: var(--green-text); }
  .heading.bold { font-weight: 700; color: var(--green-deep); -webkit-text-stroke: .5px #2f4d0c; letter-spacing: .2px; }
  .contact { font-family: "Quicksand", sans-serif; font-size: 15px; color: var(--ink); }
  .contact .label { font-family: "Fenix", serif; font-size: 13px; color: var(--green-text); font-weight: 700; margin-right: 4px; }
  .email { top: 132px; }
  .phone { top: 155px; }
  .on-dark .contact { color: var(--white); }
  .footer { position: absolute; top: 192px; font-family: "Quicksand", sans-serif; font-size: 12.5px; color: var(--ink); }
  .footer.left { left: 48px; }
  .footer.right { left: 226px; }
  .footer.light { color: var(--white); }

  /* appointment card */
  .appointment { background: var(--green); }
  .appointment .pattern { position: absolute; inset: 0; background: linear-gradient(135deg, #94c545, #86b739); }
  .date-disc { position: absolute; left: 92px; top: 32px; width: 214px; height: 214px; border-radius: 50%; background: var(--white); }
  .pet-disc {
    position: absolute; left: 260px; top: 70px; width: 78px; height: 78px; border-radius: 50%;
    background: var(--green); border: 5px solid var(--white);
  }
  .appt-title {
    position: absolute; z-index: 2; top: 13px; left: 58px; font-family: "Open Sans", sans-serif; font-weight: 800;
    font-size: 14px; color: var(--white); letter-spacing: .2px;
  }
  .day {
    position: absolute; width: 28px; height: 28px; border-radius: 50%; background: var(--white);
    font-family: "Open Sans", sans-serif; font-weight: 700; font-size: 8px; color: var(--ink);
    display: flex; align-items: center; justify-content: center;
  }
  .rule { position: absolute; height: 1px; background: var(--green); }
  .tiny { position: absolute; font-family: "Open Sans", sans-serif; font-weight: 700; font-size: 8px; color: var(--ink); }
</style>
</head>
<body>

<section class="card" style="left:64px; top:65px;">
  <svg class="bg" viewBox="0 0 383 219" aria-hidden="true">
    <path d="M0 0H383V72 l-6 6 -6 -6 -6 6 -6 -6 -6 6 -6 -6 -6 6 -6 -6 -6 6 -6 -6 -6 6 -6 -6 -6 6 -6 -6 -6 6 -6 -6 -6 6 -6 -6 -6 6 -6 -6 -6 6 -6 -6 -6 6 -6 -6 -6 6 -6 -6 -6 6 -6 -6 -6 6 -6 -6 -6 6 -6 -6 -6 6 -6 -6 -6 6 -6 -6 -6 6 -6 -6 -6 6 -6 -6 -6 6 -6 -6 -6 6 -6 -6 -6 6 -6 -6 -6 6 -6 -6 -6 6 -6 -6 -6 6 -6 -6 -6 6 -6 -6 -6 6 -6 -6 -6 6 -6 -6 -6 6 -6 -6 -6 6 -6 -6 -6 6 -6 -6 -6 6 -6 -6 -6 6 -6 -6 -6 6 -6 -6 -6 6 -6 -6 -6 6 -6 -6 -6 6 -6 -6 -6 6 -6 -6 -6 6 -6 -6 -6 6 -6 -6 -6 6 -5 -5Z" fill="var(--black)"/>
    <path d="M0 172 Q191 200 383 172 V219 H0Z" fill="var(--green)"/>
  </svg>
  <div class="brand"><span class="brand-dot"></span><span class="brand-name">Luna Brisk</span></div>
  <div class="line heading bold">Professional Grooming Services</div>
  <div class="line contact email"><span class="label">Email:</span>lunabrisk@mailvane.net</div>
  <div class="line contact phone"><span class="label">Text or call:</span>1 705 318 6642</div>
  <div class="footer left">TKV certified/member</div>
  <div class="footer right">Pet first aid certified</div>
</section>

<section class="card appointment" style="left:481px; top:65px;">
  <div class="pattern" role="img" aria-label="Repeating pattern of small line-drawn poodles"></div>
  <div class="date-disc"></div>
  <div class="pet-disc" role="img" aria-label="Line drawing of a groomed poodle with a bow"></div>
  <div class="appt-title">YOUR NEXT APPOINTMENT IS ON:</div>
  <div class="day" style="left:96px; top:37px;">MON</div>
  <div class="day" style="left:73px; top:72px;">TUE</div>
  <div class="day" style="left:67px; top:108px;">WED</div>
  <div class="day" style="left:73px; top:142px;">THU</div>
  <div class="day" style="left:91px; top:177px;">FRI</div>
  <div class="rule" style="left:129px; top:91px; width:113px;"></div>
  <div class="tiny" style="left:114px; top:124px;">AT</div>
  <div class="tiny" style="left:208px; top:118px;">AM</div>
  <div class="tiny" style="left:238px; top:118px;">PM</div>
  <div class="rule" style="left:129px; top:132px; width:125px;"></div>
</section>

<section class="card" style="left:64px; top:325px;">
  <svg class="bg" viewBox="0 0 383 219" aria-hidden="true">
    <path d="M0 0H383V92 Q191 40 0 92Z" fill="var(--black)"/>
    <path d="M0 170 Q191 202 383 170 V219 H0Z" fill="var(--green)"/>
  </svg>
  <div class="brand"><span class="brand-dot"></span><span class="brand-name">Luna Brisk</span></div>
  <div class="line heading">Professional Grooming Services</div>
  <div class="line contact email"><span class="label">Email:</span>lunabrisk@mailvane.net</div>
  <div class="line contact phone"><span class="label">Text or call:</span>1 705 318 6642</div>
  <div class="footer left">TKV certified/member</div>
  <div class="footer right">Pet first aid certified</div>
</section>

<section class="card on-dark" style="left:481px; top:325px; background:var(--black);">
  <svg class="bg" viewBox="0 0 383 219" aria-hidden="true">
    <path d="M0 170 Q191 200 383 170 V219 H0Z" fill="var(--green)"/>
  </svg>
  <div class="brand"><span class="brand-dot"></span><span class="brand-name">Luna Brisk</span></div>
  <div class="line heading">Professional Grooming Services</div>
  <div class="line contact email"><span class="label">Email:</span>lunabrisk@mailvane.net</div>
  <div class="line contact phone"><span class="label">Text or call:</span>1 705 318 6642</div>
  <div class="footer left">TKV certified/member</div>
  <div class="footer right">Pet first aid certified</div>
</section>

<section class="card" style="left:64px; top:584px;">
  <svg class="bg" viewBox="0 0 383 219" aria-hidden="true">
    <path d="M0 0H383 Q191 110 0 0Z" fill="var(--black)"/>
    <path d="M0 162 Q191 205 383 164 V219 H0Z" fill="var(--green)"/>
  </svg>
  <div class="brand"><span class="brand-dot"></span><span class="brand-name">Luna Brisk</span></div>
  <div class="line heading">Professional Grooming Services</div>
  <div class="line contact email"><span class="label">Email:</span>lunabrisk@mailvane.net</div>
  <div class="line contact phone"><span class="label">Text or call:</span>1 705 318 6642</div>
  <div class="footer left">TKV certified/member</div>
  <div class="footer right">Pet first aid certified</div>
</section>

<section class="card" style="left:481px; top:584px;">
  <svg class="bg" viewBox="0 0 383 219" aria-hidden="true">
    <defs>
      <linearGradient id="footShade" x1="0" y1="0" x2="0" y2="1">
        <stop offset="0" stop-color="#000"/>
        <stop offset="1" stop-color="#3a3a3a"/>
      </linearGradient>
    </defs>
    <path d="M0 166 Q191 196 383 160 V219 H0Z" fill="var(--green)"/>
    <path d="M0 173 Q191 203 383 167 V219 H0Z" fill="url(#footShade)"/>
  </svg>
  <div class="brand"><span class="brand-dot"></span><span class="brand-name">Luna Brisk</span></div>
  <div class="line heading bold">Professional Grooming Services</div>
  <div class="line contact email"><span class="label">Email:</span>lunabrisk@mailvane.net</div>
  <div class="line contact phone"><span class="label">Text or call:</span>1 705 318 6642</div>
  <div class="footer left light">TKV certified/member</div>
  <div class="footer right light">Pet first aid certified</div>
</section>

</body>
</html>
```